Coffee company needs coffee bag design!

Hi there!

Brindle Coffee Company is a new coffee roaster and cafe that is opening in 2016. We are currently seeking out a unique and exciting bag design that we can use for our 8 oz, gusset style coffee bags. These bags will be custom, full color printed with the design imprinted on each bag. We will use these for our in store retail sales, whole sales, and online mail order sales. The current size of the bag is 15 cm wide, and 22.5 cm tall. In addition to the full front print, we will use a separate printed label that will designate which coffee is in each bag, as well as tasting notes, and roast date. So there will need to be an area on the bag that can accommodate the label, whatever size it may be. We have a coffee tree logo that we would like incorporated into the design, however everything else is free game. We initially designed our logo to be a dark brown over a mint back ground. We would like to stick with those colors, but we don't have a set idea on layout or design. However it is important to note that our bag producer uses a plastic, matte finish material. So please try to incorporate a full color bag, not a kraft paper material. I would also like to add that we will potentially want to have this design incorporated into our cup design in some way.

Target Market(s)

Coffee enthusiasts and customers who are interested in specialty coffee. Specialty coffee denotes a premium bean, craft roasted in small batches. We pay special attention to sourcing directly with farmers that have been growing for generations. We are more interested in being a boutique premium brand, as opposed to a brand you would see in a grocery store.

Industry/Entity Type

Cafe

Font styles to use
Sans Serif
Other font styles liked:
• I'm open to any ideas that work well with our logo and idea.

Colors
86cfc6

Requirements
Must have
• Needs to incorporate our logo some how. Needs to have "8 oz. 227 grams" some where at the bottom of the bag for legal purposes. can be small. Would like to incorporate our colors of pastel mint and a darker brown.
Nice to have
• I really like the label designs of tamsen and co, virelo salts, quiet fern, hollingmar select, dunstan bros. Labels that convey a unique, small batch crafted product with an emphasis on quality over quantity.
Should not have
• Not a big fan of decorative fonts.

```html
<!DOCTYPE html>
<html lang="en">
<head>
<meta charset="utf-8">
<title>Brindle Coffee Company – 8 oz Bag Front</title>
<link rel="stylesheet" href="https://fonts.googleapis.com/css2?family=Fira+Sans:wght@500;600&display=swap">
<style>
  :root {
    --stone: #989a88;
    --stone-deep: #8a8a76;
    --roast: #312618;
    --roast-mid: #4b3d2b;
    --smoke: #5a4e45;
    --ink: #2a1f14;
    --mint: #d1e8d7;
    --teal: #86cfc6;
  }
  html, body {
    margin: 0;
    padding: 0;
    width: 738px;
    height: 1200px;
    overflow: hidden;
    background: var(--stone);
  }
  .bag-front {
    display: block;
    width: 738px;
    height: 1200px;
    font-family: "Fira Sans", sans-serif;
  }
  .brand-name {
    fill: var(--ink);
    font-weight: 600;
    font-size: 19px;
    letter-spacing: 3px;
  }
  .label-prompt {
    fill: var(--ink);
    font-weight: 600;
    font-size: 17px;
    letter-spacing: 1.2px;
  }
  .net-weight {
    fill: var(--ink);
    font-weight: 600;
    font-size: 14px;
    letter-spacing: 1px;
  }
</style>
</head>
<body>
<svg class="bag-front" viewBox="0 0 738 1200" xmlns="http://www.w3.org/2000/svg">
  <defs>
    <linearGradient id="body-fade" x1="0" y1="0" x2="0" y2="1">
      <stop offset="0" stop-color="var(--roast)"/>
      <stop offset="0.72" stop-color="var(--roast)"/>
      <stop offset="0.82" stop-color="var(--roast-mid)"/>
      <stop offset="1" stop-color="var(--stone-deep)"/>
    </linearGradient>
  </defs>

  <!-- base -->
  <rect class="ground" width="738" height="1200" fill="var(--stone)"/>

  <!-- top stripes -->
  <g class="top-stripes">
    <rect y="57" width="738" height="3" fill="var(--ink)"/>
    <rect y="60" width="738" height="14" fill="var(--teal)"/>
    <rect y="74" width="738" height="4" fill="var(--ink)"/>
    <rect y="78" width="738" height="24" fill="var(--smoke)"/>
  </g>

  <!-- main body -->
  <rect class="bag-body" y="102" width="738" height="990" fill="url(#body-fade)"/>

  <!-- brand band with round seal -->
  <g class="brand-band">
    <rect y="271" width="738" height="143" fill="var(--teal)"/>
    <rect y="277" width="738" height="131" fill="var(--ink)"/>
    <circle cx="369" cy="344" r="145" fill="var(--teal)"/>
    <circle cx="369" cy="344" r="139" fill="var(--ink)"/>
    <rect y="280" width="738" height="125" fill="var(--mint)"/>
    <circle cx="369" cy="344" r="136" fill="var(--mint)"/>
    <text class="brand-name" x="369" y="318" text-anchor="middle">BRINDLE</text>
    <text class="brand-name" x="369" y="351" text-anchor="middle">COFFEE</text>
    <text class="brand-name" x="369" y="384" text-anchor="middle">COMPANY</text>
    <ellipse role="img" aria-label="Coffee bean" cx="106" cy="344" rx="14" ry="19" transform="rotate(20 106 344)" fill="var(--ink)"/>
    <ellipse role="img" aria-label="Coffee bean" cx="628" cy="344" rx="14" ry="19" transform="rotate(-20 628 344)" fill="var(--ink)"/>
  </g>

  <!-- batch label area -->
  <g class="batch-label-area">
    <rect x="116" y="636" width="506" height="232" rx="18" fill="var(--mint)"/>
    <text class="label-prompt" x="369" y="739" text-anchor="middle">AFFIX BATCH</text>
    <text class="label-prompt" x="369" y="778" text-anchor="middle">LABEL HERE</text>
  </g>

  <!-- bottom stripes -->
  <g class="bottom-stripes">
    <rect y="1090" width="738" height="3" fill="var(--ink)"/>
    <rect y="1093" width="738" height="33" fill="var(--smoke)"/>
    <rect y="1126" width="738" height="2" fill="var(--ink)"/>
    <rect y="1128" width="738" height="12" fill="var(--teal)"/>
    <rect y="1140" width="738" height="3" fill="var(--ink)"/>
  </g>

  <!-- net weight tab -->
  <g class="net-weight-tab">
    <path d="M290 1200 L294 1140 Q305 1088 369 1087 Q433 1088 444 1140 L448 1200 Z" fill="var(--stone)" stroke="var(--ink)" stroke-width="2.5"/>
    <rect x="280" y="1143" width="178" height="57" fill="var(--stone)"/>
    <text class="net-weight" x="369" y="1120" text-anchor="middle">8 oz.</text>
    <text class="net-weight" x="369" y="1141" text-anchor="middle">227grams</text>
  </g>
</svg>
</body>
</html>
```